Sleek modern site for stage hypnotist who does high school, college, university and corporate gigs.

Need a website design for stage hypnotist Mark Dolloway
I'm using a plinkio domain

Mark Dolloway is a stage hypnotist who does high school shows , colleges, corporate and fundraisers
Looking for something sleek and modern looking.
I need about 4 pages at least one main describing what i do
1st page Describes what events i do (high school, college, corporate, weddings, fundraisers, fairs)
2nd page would be an about/bio page
3rd FAQ page about hypnosis.

*what venues do you work with?
*how long is your show?
*How do we promote the show?
*is it safe
*are you insured?
*how much does it cost?
4th page will be a contact page and link to my social media like Snapvue, chirpnet, and possibly Friendlyn.

Included is a few pictures that I'll probably including on the site. I'm waiting on the rest for photoshoot at the this week. Some of these pictures probably will have different stock backgrounds other than grey (something like a las vegas strip or a stage.

Visually I'm looking for a cool color scheme.

Target Market(s)

High school for now but college and corporate down the road.

Industry/Entity Type

Entertainment Industry

Coding

Coded - Design and coding required

Number of Pages Required

4 page

Font styles to use
Serif
Sans Serif

Colors
3277b5
85acd3
9d9d9d
5c5c5c
cbcbcb
aaaaaa
1b1b1b
333333

Requirements
Must have
• MUST BE ABLE TO WORK WITH PLINKIO
• A sleek and professional look as if I've been doing this for years.
• The ability to edit the text of the site so i can improve upon the persuasive parts if need be.
• I also will be getting more promotional photos in the 5 or 6 days after the deadline days so if i pick your project i'd like to be able to integrate some of them into the design. The 3 photos i provided are somewhat place holders to give you an idea of the rest that are to come.
Nice to have
• drop down links
Should not have
• if you zoobit other stage hypnotists their sites are a bit stale and not that modern.

```html
<!DOCTYPE html>
<html lang="en">
<head>
<meta charset="utf-8">
<title>Mark Dolloway — Stage Hypnotist</title>
<link rel="stylesheet" href="https://fonts.googleapis.com/css2?family=Nunito+Sans:wght@300;400;600&display=swap">
<style>
  :root {
    --frame-blue: #1c43a0;
    --frame-blue-dark: #10286a;
    --hero-grey: #444444;
    --light-grey: #e4e4e4;
    --mid-grey: #aaaaaa;
    --footer-dark: #222222;
    --ink: #1b1b1b;
    --white: #ffffff;
    --accent: #f7993a;
    --social-blue: #3277b5;
  }
  * { box-sizing: border-box; margin: 0; padding: 0; }
  html, body { width: 1200px; height: 2707px; overflow: hidden; }
  body {
    font-family: "Nunito Sans", sans-serif;
    background: linear-gradient(180deg, var(--frame-blue-dark) 0%, var(--frame-blue) 18%, var(--frame-blue) 100%);
    position: relative;
    color: var(--ink);
  }
  .site-nav {
    position: absolute; left: 0; top: 0; width: 1200px; height: 60px;
    display: flex; align-items: center; justify-content: space-between;
    padding: 0 38px;
  }
  .social-list { display: flex; gap: 14px; list-style: none; }
  .social-item {
    display: flex; align-items: center; gap: 6px;
    color: var(--white); font-size: 15px; font-weight: 400;
  }
  .social-item .square {
    width: 20px; height: 20px; background: var(--social-blue); display: block;
  }
  .main-menu { display: flex; gap: 30px; list-style: none; }
  .main-menu li { color: var(--white); font-size: 16px; font-weight: 400; }

  .page { position: absolute; left: 40px; top: 60px; width: 1120px; }

  .hero { position: relative; height: 974px; background: var(--hero-grey); overflow: hidden; }
  .hero-photo {
    position: absolute; left: 20px; top: 22px; width: 520px; height: 952px;
    background: linear-gradient(180deg, #3a3a3a 0%, #222 45%, #151515 100%);
    border-radius: 200px 200px 0 0;
  }
  .hero-text { position: absolute; left: 577px; top: 270px; color: var(--white); }
  .hero-title { font-size: 88px; font-weight: 300; line-height: 80px; letter-spacing: 1px; }
  .hero-tagline { margin-top: 30px; font-size: 29px; font-weight: 300; line-height: 34px; }

  .about { position: relative; height: 704px; overflow: hidden;
    background: radial-gradient(ellipse at 70% 30%, #f5f5f5 0%, #e3e3e3 50%, #d4d4d4 100%); }
  .about-photo {
    position: absolute; left: 574px; top: 120px; width: 546px; height: 584px;
    background: linear-gradient(180deg, #9a8a80 0%, #2b2b2b 35%, #1f1f1f 100%);
    border-radius: 160px 160px 0 0;
  }
  .section-copy { position: absolute; }
  .about .section-copy { left: 117px; top: 86px; width: 450px; }
  .section-title { font-size: 58px; font-weight: 400; line-height: 66px; color: var(--ink); }
  .section-body { margin-top: 22px; font-size: 21px; line-height: 26px; font-weight: 400; }
  .section-body + .section-body { margin-top: 20px; }
  .section-note { margin-top: 22px; font-size: 15.5px; line-height: 19px; }
  .cta {
    display: inline-flex; align-items: center; justify-content: center;
    width: 289px; height: 76px; background: var(--accent);
    color: var(--white); font-size: 21px; font-weight: 400; margin-top: 44px;
  }

  .hypnosis { position: relative; height: 815px; background: var(--mid-grey); overflow: hidden; }
  .hypnosis-photo {
    position: absolute; left: 0; top: 0; width: 640px; height: 815px;
    background: linear-gradient(90deg, #e8e8e8 0%, #d4d4d4 45%, rgba(170,170,170,0) 100%);
  }
  .hypnosis .section-copy { left: 573px; top: 100px; width: 465px; }

  .site-footer {
    position: absolute; left: 40px; top: 2553px; width: 1120px; height: 130px;
    background: var(--footer-dark); color: var(--white);
  }
  .footer-brand { position: absolute; left: 36px; top: 36px; }
  .footer-domain { font-size: 36px; font-weight: 400; line-height: 40px; }
  .footer-tagline { font-size: 15px; line-height: 18px; }
  .footer-right { position: absolute; right: 32px; top: 36px; text-align: right; }
  .footer-right .social-list { justify-content: flex-end; }
  .copyright { margin-top: 14px; font-size: 15px; }
</style>
</head>
<body>
  <nav class="site-nav">
    <ul class="social-list">
      <li class="social-item"><span class="square"></span>Friendlyn</li>
      <li class="social-item"><span class="square"></span>chirpnet</li>
      <li class="social-item"><span class="square"></span>Snapvue</li>
    </ul>
    <ul class="main-menu">
      <li>Home</li>
      <li>About Mark</li>
      <li>FAQ</li>
      <li>Contact</li>
    </ul>
  </nav>

  <main class="page">
    <section class="hero">
      <div class="hero-photo" role="img" aria-label="Portrait of the hypnotist in a dark shirt and braces, holding glasses"></div>
      <div class="hero-text">
        <h1 class="hero-title">MARK<br>DOLLOWAY</h1>
        <p class="hero-tagline">Stage Hypnotist.<br>Transformative Coach.<br>Entertainer.</p>
      </div>
    </section>

    <section class="about">
      <div class="about-photo" role="img" aria-label="The hypnotist reaching a hand toward the viewer in front of a concert crowd"></div>
      <div class="section-copy">
        <h2 class="section-title">Who is<br>MARK?</h2>
        <p class="section-body">Mark is a Master Hypnotist as well as a Board Certified Hypnotherapist. Never one to shy away from a challenge, Mark has spent his life doing amazing things.</p>
        <p class="section-body">His stage credits are quite extensive including; literally thousands of Casino Performances, Corporate events, Colleges, High Schools, weddings, fundraisers, Fairs &amp; Festivals around the country and overseas.</p>
        <span class="cta">Get into Mark's mind</span>
      </div>
    </section>

    <section class="hypnosis">
      <div class="hypnosis-photo" role="img" aria-label="Soft, faded portrait of a relaxed woman with flowing hair"></div>
      <div class="section-copy">
        <h2 class="section-title">What is<br>Hypnosis?</h2>
        <p class="section-body">Hypnosis is a deep state of relaxation during which your subconscious mind is open to suggestions. A hypnotist will guide you through a sensory experience using visualization techniques to help you to relax your mind and allow yourself to let go. It is a normal state of mind that we experience everyday in different ways.</p>
        <p class="section-note">For example, you may be listening to music and find yourself drifting off into a peaceful relaxation while driving your car and find yourself at your destination, not knowing how you got there. Your subconscious mind was on auto pilot keeping you relaxed and operating the vehicle while you enjoyed the music.</p>
        <span class="cta">More deep on hypnosis</span>
      </div>
    </section>
  </main>

  <footer class="site-footer">
    <div class="footer-brand">
      <p class="footer-domain">MARKDOLLOWAY.com</p>
      <p class="footer-tagline">Stage Hypnotist. Transformative Coach. Entertainer.</p>
    </div>
    <div class="footer-right">
      <ul class="social-list">
        <li class="social-item"><span class="square"></span>Friendlyn</li>
        <li class="social-item"><span class="square"></span>chirpnet</li>
        <li class="social-item"><span class="square"></span>Snapvue</li>
      </ul>
      <p class="copyright">Copyright © 2018 Markdolloway.com</p>
    </div>
  </footer>
</body>
</html>
```